we need PDF and print ready letterheads, dupplicated 5 times with different company details of different companies. All the companies are properties developments and no need for fancy logos (any reasonable shape is ok). Then simply change the companies details (names and company number) and the colour scheme slightly. I will supply the details.

The print ready should be 300dpi, and must have cropped marks.

Should be an easy job!

```html
<!DOCTYPE html>
<html lang="en">
<head>
<meta charset="UTF-8">
<title>Letterhead</title>
<link rel="stylesheet" href="https://fonts.googleapis.com/css2?family=Montserrat:wght@700&family=PT+Sans:wght@400&display=swap">
<style>
  :root {
    --brand: #283891;
    --ink: #111111;
    --paper: #ffffff;
  }
  * { margin: 0; padding: 0; box-sizing: border-box; }
  html, body {
    width: 927px;
    height: 1200px;
    overflow: hidden;
    background: var(--paper);
  }
  .letterhead {
    position: relative;
    width: 927px;
    height: 1200px;
    background: var(--paper);
    overflow: hidden;
  }
  .brand {
    position: absolute;
    left: 87px;
    top: 46px;
  }
  .brand-mark {
    display: block;
    width: 44px;
    height: 44px;
    background: var(--brand);
  }
  .brand-name {
    margin-top: 11px;
    font-family: "Montserrat", sans-serif;
    font-weight: 700;
    font-size: 15px;
    letter-spacing: 0.1px;
    color: var(--ink);
    white-space: nowrap;
  }
  .company-details {
    position: absolute;
    left: 689px;
    top: 30px;
    width: 215px;
    font-family: "PT Sans", sans-serif;
    font-size: 14.4px;
    line-height: 27.2px;
    color: var(--ink);
  }
  .edge-bar {
    position: absolute;
    right: 0;
    top: 0;
    width: 13px;
    height: 182px;
    background: var(--brand);
  }
  .footer-wave {
    position: absolute;
    left: 0;
    bottom: 0;
    width: 927px;
    height: 110px;
    display: block;
  }
  .footer-text {
    position: absolute;
    left: 0;
    right: 0;
    top: 1172px;
    text-align: center;
    padding-left: 17px;
    font-family: "PT Sans", sans-serif;
    font-size: 14.4px;
    color: var(--paper);
  }
</style>
</head>
<body>
<div class="letterhead">
  <div class="brand">
    <span class="brand-mark"></span>
    <p class="brand-name">THE COMPANY NAME</p>
  </div>

  <p class="company-details">
    Lorem ipsum dolor sit amet,<br>
    consectetuer adipiscing elit, sed<br>
    diam nonummy nibh euismod<br>
    tincidunt ut laoreet dolore<br>
    magna aliquam erat volutpat. Ut
  </p>

  <div class="edge-bar"></div>

  <svg class="footer-wave" viewBox="0 1090 927 110" preserveAspectRatio="none" aria-hidden="true">
    <path d="M0 1154 C 160 1146, 330 1151, 480 1151 C 700 1150, 860 1125, 927 1094 L 927 1200 L 0 1200 Z" fill="var(--brand)"/>
  </svg>

  <p class="footer-text">Lorem ipsum</p>
</div>
</body>
</html>
```